Roaming outings business card

please see website
www.roamingoutings.comau

info needed on card
Keiran Voss
Ph
email
Adventure Riding GPS trails

please use my logo and colours off my site

Business

Keiran Voss
keiran@roamingoutings.com

```html
<!DOCTYPE html>
<html lang="en">
<head>
<meta charset="utf-8">
<title>Roaming outings – business card</title>
<link rel="stylesheet" href="https://fonts.googleapis.com/css2?family=Arimo:wght@400;700&display=swap">
<style>
  :root {
    --stage: #2b2b2b;
    --card-black: #0b0b0b;
    --card-white: #ffffff;
    --brand-yellow: #f7cf12;
    --text-dark: #1a1a1a;
    --text-grey: #555555;
    --rule-grey: #bdbdbd;
    --text-light: #f2f2f2;
  }
  * { box-sizing: border-box; margin: 0; padding: 0; }
  html, body {
    width: 1200px; height: 750px; overflow: hidden;
    background: var(--stage);
    font-family: "Arimo", Arial, sans-serif;
  }
  .stage {
    position: relative; width: 1200px; height: 750px;
    display: flex; align-items: center; justify-content: center; gap: 60px;
  }
  .card {
    position: relative; width: 500px; height: 286px; overflow: hidden;
    box-shadow: 0 14px 30px rgba(0,0,0,.55);
  }
  /* back side */
  .card--back { background: var(--card-black); color: var(--text-light); }
  .card--back .brand { position: absolute; top: 106px; left: 0; right: 0; justify-content: center; }
  .card--back .brand__name { color: var(--text-light); }
  .card--back .tagline {
    position: absolute; top: 178px; left: 0; right: 0; text-align: center;
    font-size: 13px; color: var(--text-light);
  }
  /* shared brand lockup */
  .brand { display: flex; align-items: center; gap: 12px; }
  .brand__dot { width: 30px; height: 30px; border-radius: 50%; background: var(--brand-yellow); flex: none; }
  .brand__name { font-size: 30px; font-weight: 700; letter-spacing: .5px; }
  /* front side */
  .card--front { background: var(--card-white); }
  .card--front .brand { position: absolute; top: 36px; left: 130px; }
  .card--front .brand__name { color: var(--text-dark); }
  .holder {
    position: absolute; top: 120px; left: 40px; width: 170px; text-align: right;
    font-size: 20px; color: var(--brand-yellow);
  }
  .divider { position: absolute; top: 98px; left: 226px; width: 1px; height: 66px; background: var(--rule-grey); }
  .contacts { position: absolute; top: 97px; left: 242px; list-style: none; }
  .contacts li {
    display: flex; align-items: center; gap: 8px;
    font-size: 13px; color: var(--text-grey); line-height: 22px;
  }
  .contacts svg { width: 12px; height: 12px; flex: none; }
  .band { position: absolute; left: 0; bottom: 0; width: 500px; height: 286px; }
  .card--front .tagline {
    position: absolute; right: 44px; bottom: 20px;
    font-size: 13px; color: var(--text-light);
  }
</style>
</head>
<body>
<main class="stage">
  <section class="card card--back" aria-label="Card back">
    <div class="brand">
      <span class="brand__dot"></span>
      <span class="brand__name">Roaming outings</span>
    </div>
    <p class="tagline">Adventure Riding GPS trails</p>
  </section>

  <section class="card card--front" aria-label="Card front">
    <svg class="band" viewBox="0 0 500 286" aria-hidden="true">
      <path d="M0 232 Q260 222 500 176 L500 286 L0 286 Z" fill="var(--brand-yellow)"/>
      <path d="M0 242 Q262 232 500 188 L500 286 L0 286 Z" fill="var(--card-black)"/>
    </svg>
    <div class="brand">
      <span class="brand__dot"></span>
      <span class="brand__name">Roaming outings</span>
    </div>
    <p class="holder">Keiran Voss</p>
    <span class="divider"></span>
    <ul class="contacts">
      <li>
        <svg viewBox="0 0 12 12"><path d="M3 1 L5 3 L4 5 Q5 7 7 8 L9 7 L11 9 L9 11 Q3 10 1 3 Z" fill="var(--brand-yellow)"/></svg>
        555 0142 8890
      </li>
      <li>
        <svg viewBox="0 0 12 12"><rect x="1" y="2.5" width="10" height="7" fill="var(--brand-yellow)"/><path d="M1 2.5 L6 6.5 L11 2.5" stroke="#fff" fill="none"/></svg>
        keiran@roamingoutings.com
      </li>
      <li>
        <svg viewBox="0 0 12 12"><circle cx="6" cy="6" r="5" fill="var(--brand-yellow)"/><path d="M1 6 H11 M6 1 Q3 6 6 11 M6 1 Q9 6 6 11" stroke="#fff" stroke-width=".8" fill="none"/></svg>
        www.roamingoutings.comau
      </li>
    </ul>
    <p class="tagline">Adventure Riding GPS trails</p>
  </section>
</main>
</body>
</html>
```